2 sided postcard for New Internet Customers

We would like a design for a two sided postcard (with room for mailing label), dimensions 9 1/4 by 6 1/4 to be sent via US Mail.

The postcard needs to include our logo (attached) and the text
Fiber Optic Internet
555-219-8063
http://www.brightwirenet.example
Speeds up to 1 Gig, with packages starting at $55

These will be sent to people who do not have our service.

Since this is going to be "junk mail" we probably only have 1 second or less to capture someone's attention to encourage them to read the entire postcard.

We are a "mom and pop" telecommunications company that provides internet, phone, and television services on the fiber optic network that we designed, built, and maintain.

We started as a dial up ISP in 1995, and have extraordinary technical support based in Freeport PA, our customers actually get the speeds they pay for, and our service is highly reliable.

We have a slogan (which you can choose to use or ignore) which is
"I Went Fast with Kornwell"

Existing customers can earn a $50 credit for every new customer they refer to us. Unlike most large cable and internet companies we have very happy customers... some who have stayed with us for decades.

I've attached our previous postcard, which I really dislike. It does have a blank spot for where the mailing label should go.

Target Market(s)

New Internet Customers in Western Pennsylvania

Industry/Entity Type

Internet

Font styles to use
Other font styles liked:
• Just match our logo.

Colors

Designer to choose colors to be used in the design.

Requirements
Must have
• The postcard needs to include our logo, and the text Fiber Optic Internet 555-219-8063 http://www.brightwirenet.example Speeds up to 1 Gig, with packages starting at $55
Nice to have
• The colors and fonts should look good with our logo.
Should not have
• Should not have small print or lots of text. Both sides need to capture attention.

```html
<!DOCTYPE html>
<html lang="en">
<head>
<meta charset="utf-8">
<title>Kornwell Fiber Optic Internet Postcard</title>
<link href="https://fonts.googleapis.com/css2?family=Poppins:ital,wght@0,400;0,600;0,700;1,700;1,800&display=swap" rel="stylesheet">
<style>
  :root {
    --page: #e8e8e8;
    --card-dark: #3d3d3f;
    --card-deep: #2c2c2e;
    --teal: #8fdde0;
    --teal-band: #3f6a6a;
    --white: #ffffff;
    --silver: #d9d9d9;
    --label-white: #f7f7f7;
    --brand-blue: #2f7fc8;
    --ink: #222222;
    --photo-blue: #3a48c8;
  }
  * { box-sizing: border-box; margin: 0; padding: 0; }
  html, body { width: 1200px; height: 800px; overflow: hidden; }
  body {
    background: var(--page);
    font-family: "Poppins", sans-serif;
    position: relative;
  }
  .postcard {
    position: absolute;
    width: 560px;
    height: 378px;
    top: 211px;
    overflow: hidden;
    box-shadow: 0 4px 10px rgba(0,0,0,0.18);
  }
  /* Front side */
  .postcard--front { left: 27px; background: var(--card-dark); }
  .front__photo {
    position: absolute; inset: 0 0 110px 0;
    background:
      radial-gradient(ellipse 45% 55% at 30% 55%, rgba(58,72,200,0.55), transparent 70%),
      radial-gradient(ellipse 30% 40% at 75% 25%, rgba(200,200,200,0.35), transparent 70%),
      linear-gradient(180deg, #6a6a6c 0%, #4a4a4c 60%, var(--card-dark) 100%);
  }
  .front__copy {
    position: absolute; right: 22px; top: 196px;
    text-align: right;
  }
  .front__eyebrow {
    color: var(--teal);
    font-size: 12.5px;
    font-weight: 400;
    letter-spacing: 3.6px;
    margin-bottom: 14px;
  }
  .front__headline {
    color: var(--silver);
    font-size: 25px;
    font-weight: 700;
    line-height: 1.45;
    text-shadow: 0 0 6px rgba(255,255,255,0.25);
  }
  .front__headline .accent { color: var(--teal); }
  .front__headline .price { font-size: 33px; color: var(--silver); letter-spacing: 1px; }
  .front__contact {
    position: absolute; right: 22px; bottom: 22px;
    display: flex; gap: 22px;
    color: var(--silver); font-size: 9.5px;
  }
  .front__contact span { display: flex; align-items: center; gap: 6px; }
  .front__contact svg { width: 10px; height: 10px; }

  /* Back side */
  .postcard--back { left: 613px; background: var(--card-dark); }
  .back__shapes { position: absolute; inset: 0; }
  .back__brand {
    position: absolute; right: 30px; top: 22px;
    text-align: center;
  }
  .brand__row { display: flex; align-items: center; gap: 6px; justify-content: center; }
  .brand__dot { width: 22px; height: 22px; border-radius: 50%; background: var(--brand-blue); }
  .brand__name { font-size: 13px; font-weight: 400; color: var(--ink); }
  .brand__url { font-size: 7px; color: var(--ink); margin-left: 22px; }
  .brand__service {
    margin-top: 3px; font-size: 10px; font-weight: 600; color: var(--brand-blue);
  }
  .brand__phone { font-size: 8.5px; font-weight: 700; color: var(--ink); margin-top: 2px; }
  .back__offer {
    position: absolute; right: 34px; top: 200px; text-align: right;
    color: var(--white);
  }
  .offer__amount {
    font-size: 38px; font-weight: 800; font-style: italic; line-height: 1.1;
    text-shadow: 0 0 8px rgba(255,255,255,0.35);
  }
  .offer__detail { font-size: 21px; font-weight: 700; font-style: italic; line-height: 1.5; }
  .back__slogan {
    position: absolute; left: 200px; bottom: 28px;
    font-size: 11px; font-weight: 700; font-style: italic; color: var(--white);
  }
  .quote-mark {
    position: absolute; font-size: 70px; font-weight: 800; line-height: 1;
    color: rgba(255,255,255,0.22);
  }
  .quote-mark--open { left: 196px; bottom: -14px; }
  .quote-mark--close { left: 322px; bottom: 6px; }
</style>
</head>
<body>

<section class="postcard postcard--front" aria-label="Postcard front">
  <div class="front__photo" role="img" aria-label="Photograph of fiber optic cables with glowing blue light plugged into network equipment"></div>
  <div class="front__copy">
    <p class="front__eyebrow">FIBER OPTIC INTERNET</p>
    <h1 class="front__headline">Speed Up To <span class="accent">1 Gig</span><br>
      with packages <span class="accent">starting at</span> <span class="price">$55</span></h1>
  </div>
  <div class="front__contact">
    <span>www.brightwirenet.example
      <svg viewBox="0 0 10 10" fill="none" stroke="currentColor" stroke-width="0.8"><circle cx="5" cy="5" r="4"/><ellipse cx="5" cy="5" rx="1.8" ry="4"/><line x1="1" y1="5" x2="9" y2="5"/></svg>
    </span>
    <span>555-219-8063
      <svg viewBox="0 0 10 10" fill="currentColor"><path d="M2 1l2 .2.6 2-1.1.8a6 6 0 0 0 2.5 2.5l.8-1.1 2 .6.2 2-1 1C4.5 8.8 1.2 5.5 1 2z"/></svg>
    </span>
  </div>
</section>

<section class="postcard postcard--back" aria-label="Postcard back">
  <svg class="back__shapes" viewBox="0 0 560 378" preserveAspectRatio="none" aria-hidden="true">
    <rect width="560" height="378" fill="var(--card-dark)"/>
    <polygon points="0,86 560,117 560,164 0,265" fill="var(--teal-band)"/>
    <polygon points="0,0 560,0 560,117 0,86" fill="var(--label-white)"/>
    <rect y="260" width="560" height="118" fill="var(--card-deep)" opacity="0.35"/>
  </svg>
  <div class="back__brand">
    <div class="brand__row"><span class="brand__dot"></span><span class="brand__name">Kornwell, Inc.</span></div>
    <p class="brand__url">www.kornwell.example</p>
    <p class="brand__service">Internet Services</p>
    <p class="brand__phone">(555) 402-7716</p>
  </div>
  <div class="back__offer">
    <p class="offer__amount">Get $50</p>
    <p class="offer__detail">for referring us<br>to new customer</p>
  </div>
  <span class="quote-mark quote-mark--open">“</span>
  <span class="quote-mark quote-mark--close">”</span>
  <p class="back__slogan">I Went Fast with Kornwell</p>
</section>

</body>
</html>
```